business cards for a real estate investment company
Corva Homebuyers
Hi,
Can you check the draft #130, #131, #132, #133, #134, #135 and #136.
Thanks
Hello vostrapixel. I was really hoping to see some updated designs. I like what you've done so far and was hoping to give you the money. The drafts i mentioned above are almost perfect except< again, I'd love to see the term "Homebuilders" along with the logo so it's more obvious what services we provide. Thank you and I hope to see some more great work
TK/RPF/NW Team
Hello. One more note! I really like #45 as well. Same notes and changes apply. Thanks again
Hi vostrapixel. I really love design number 63. One thing I would like you to incorporate is "Homebuyers LLC". Maybe place the phrase somewhere around the corva logo. I'll trust your sensibility. Looking back, I really like number 47 as well, but with 63's backside, and again including "Homebuyers LLC". Thank you so much and I look forward to your modifications.

```html
<!DOCTYPE html>
<html lang="en">
<head>
<meta charset="utf-8">
<title>Corva Homebuyers – Business Cards</title>
<link href="https://fonts.googleapis.com/css2?family=Montserrat:wght@400;500;700;800&display=swap" rel="stylesheet">
<style>
  :root {
    --page-bg: #eef0f2;
    --card-bg: #ffffff;
    --brand-blue: #1d5fb3;
    --deep-blue: #0f3f8c;
    --light-blue: #3d8fd9;
    --brand-green: #6aab2e;
    --text-dark: #3a3f47;
    --text-light: #ffffff;
  }
  * { margin: 0; padding: 0; box-sizing: border-box; }
  html, body {
    width: 1200px; height: 980px; overflow: hidden;
    background: var(--page-bg);
    font-family: "Montserrat", sans-serif;
  }
  .canvas { position: relative; width: 1200px; height: 980px; }
  .card {
    position: absolute; left: 215px;
    width: 770px; height: 440px;
    background: var(--card-bg);
    border-radius: 22px;
    overflow: hidden;
    box-shadow: 0 6px 22px rgba(0,0,0,0.12);
  }
  .card--front { top: 30px; }
  .card--back { top: 510px; }

  .brand { position: absolute; }
  .wordmark {
    font-family: "Montserrat", sans-serif;
    font-weight: 800;
    color: var(--brand-blue);
    letter-spacing: -1px;
    line-height: 1;
  }
  .tagline {
    font-family: "Montserrat", sans-serif;
    font-weight: 700;
    color: var(--brand-green);
    text-transform: uppercase;
    line-height: 1;
  }

  .card--front .brand {
    left: 0; right: 0; top: 138px; text-align: center;
  }
  .card--front .wordmark { font-size: 104px; }
  .card--front .tagline { font-size: 22px; letter-spacing: 7px; margin-top: 18px; }

  .card--back .brand { left: 44px; top: 30px; }
  .card--back .wordmark { font-size: 56px; }
  .card--back .tagline { font-size: 14px; letter-spacing: 4px; margin-top: 8px; padding-left: 3px; }

  .contact-list {
    position: absolute; left: 48px; top: 130px;
    list-style: none;
  }
  .contact-item {
    display: flex; align-items: center; gap: 12px;
    font-size: 17px; font-weight: 500; color: var(--text-dark);
    letter-spacing: 1.5px; margin-bottom: 10px;
  }
  .contact-icon {
    width: 24px; height: 24px; border-radius: 50%;
    background: var(--brand-blue);
    display: flex; align-items: center; justify-content: center;
    flex-shrink: 0;
  }
  .wave { position: absolute; left: 0; top: 0; width: 770px; height: 440px; }
  .person {
    position: absolute; right: 40px; bottom: 34px;
    text-align: right; color: var(--text-light);
    letter-spacing: 2px; text-transform: uppercase;
  }
  .person-name { font-size: 19px; font-weight: 700; }
  .person-title { font-size: 14px; font-weight: 400; margin-top: 4px; }
</style>
</head>
<body>
<div class="canvas">

  <section class="card card--front" aria-label="Card front">
    <div class="brand">
      <div class="wordmark">Corva</div>
      <div class="tagline">Homebuyers LLC</div>
    </div>
  </section>

  <section class="card card--back" aria-label="Card back">
    <svg class="wave" viewBox="0 0 770 440" aria-hidden="true">
      <defs>
        <linearGradient id="blueBand" x1="0" y1="0" x2="1" y2="1">
          <stop offset="0" stop-color="#3d8fd9"/>
          <stop offset="0.55" stop-color="#1d5fb3"/>
          <stop offset="1" stop-color="#0f3f8c"/>
        </linearGradient>
      </defs>
      <path d="M0,250 C180,330 420,380 770,235 L770,440 L0,440 Z" fill="url(#blueBand)"/>
      <path d="M0,238 C190,318 430,360 770,218 L770,232 C430,372 180,330 0,250 Z" fill="var(--brand-green)"/>
      <path d="M0,262 C200,340 430,392 770,250" fill="none" stroke="#ffffff" stroke-width="3" opacity="0.55"/>
    </svg>

    <div class="brand">
      <div class="wordmark">Corva</div>
      <div class="tagline">Homebuyers LLC</div>
    </div>

    <ul class="contact-list">
      <li class="contact-item">
        <span class="contact-icon">
          <svg width="13" height="13" viewBox="0 0 24 24"><path fill="#fff" d="M6.6 10.8a15.1 15.1 0 0 0 6.6 6.6l2.2-2.2c.3-.3.7-.4 1-.2 1.1.4 2.300.6 3.6.6.6 0 1 .4 1 1V20c0 .6-.4 1-1 1A17 17 0 0 1 3 4c0-.6.4-1 1-1h3.5c.6 0 1 .4 1 1 0 1.3.2 2.5.6 3.6.1.3 0 .7-.2 1z"/></svg>
        </span>555-014-2290
      </li>
      <li class="contact-item">
        <span class="contact-icon">
          <svg width="13" height="13" viewBox="0 0 24 24"><path fill="#fff" d="M3 5h18v14H3z M3 5l9 8 9-8" stroke="#1d5fb3" stroke-width="1.6"/></svg>
        </span>hello@corvahomebuyers.com
      </li>
      <li class="contact-item">
        <span class="contact-icon">
          <svg width="13" height="13" viewBox="0 0 24 24"><circle cx="12" cy="12" r="9" fill="none" stroke="#fff" stroke-width="2"/><path d="M3 12h18M12 3c3 3 3 15 0 18M12 3c-3 3-3 15 0 18" fill="none" stroke="#fff" stroke-width="1.5"/></svg>
        </span>www.corvahomebuyers.com
      </li>
    </ul>

    <div class="person">
      <div class="person-name">Dan Torquell</div>
      <div class="person-title">Managing Partner</div>
    </div>
  </section>

</div>
</body>
</html>
```